Flyer to Restuarant

This is for a new Jamaican restaurant called Mango Harbor Kitchen. It should have beach scene with coconut trees. pictures of jerk chicken, oxtails and fish platters. The Jamaican flag or The flyer should the colors of the jamaican flag. Black, green and yellow. Feel free to input own ideas.

Industry/Entity Type

Restaurant

Requirements
Must have
• It should have beach scene with coconut trees in the daytime. pictures of jerk chicken, oxtails and fish platters. The Jamaican flag or The flyer should the colors of the jamaican flag. Black, green and yellow.

```html
<!DOCTYPE html>
<html lang="en">
<head>
<meta charset="utf-8">
<title>Mango Harbor Kitchen – Flyer</title>
<link href="https://fonts.googleapis.com/css2?family=Arimo:wght@400;700&family=Roboto+Condensed:wght@700&display=swap" rel="stylesheet">
<style>
  :root {
    --backdrop: #ece8e1;
    --flyer-black: #050505;
    --jam-yellow: #eeea12;
    --jam-green: #4b7a2c;
    --brand-green: #4e7d33;
    --ink: #0b0b0b;
    --white: #ffffff;
    --sky: #6fa6df;
    --sea: #79c9c9;
    --sand: #efe6d3;
  }
  * { margin: 0; padding: 0; box-sizing: border-box; }
  html, body {
    width: 1200px; height: 900px; overflow: hidden;
    background: var(--backdrop);
  }
  .canvas { position: relative; width: 1200px; height: 900px; }
  .flyer {
    position: absolute; left: 83px; top: 27px;
    width: 586px; height: 831px;
    background: var(--flyer-black);
    overflow: hidden;
    font-family: "Arimo", Arial, sans-serif;
    color: var(--ink);
  }
  .flyer-shapes { position: absolute; inset: 0; width: 586px; height: 831px; }
  .food-photo {
    position: absolute;
    border: 3px solid var(--flyer-black);
    border-radius: 8px 26px 8px 22px;
  }
  .food-photo--oxtail {
    left: 235px; top: 374px; width: 160px; height: 114px;
    background: linear-gradient(160deg, #e9e2d6 0%, #7a4526 45%, #4a2412 75%, #d9d2c6 100%);
  }
  .food-photo--jerk {
    left: 410px; top: 373px; width: 160px; height: 115px;
    background: linear-gradient(150deg, #c99a3a 0%, #8f5a1e 40%, #4e3a17 70%, #b07b2a 100%);
  }
  .food-photo--fish {
    left: 319px; top: 500px; width: 174px; height: 125px;
    background: linear-gradient(140deg, #4f6a35 0%, #c9a772 35%, #d2463a 60%, #6f9440 100%);
  }
  .headline {
    position: absolute; left: 14px; top: 508px; width: 316px;
    text-align: center;
    font-weight: 700; font-size: 24.5px; line-height: 34px;
    letter-spacing: -0.2px;
  }
  .body-copy {
    position: absolute; left: 23px; top: 596px; width: 420px;
    font-size: 13.1px; line-height: 20.8px;
  }
  .contact {
    position: absolute; left: 33px; top: 768px;
    font-weight: 700; font-size: 18px;
  }
  .brand-name {
    position: absolute; left: 338px; top: 721px; width: 250px;
    text-align: center;
    font-family: "Roboto Condensed", "Arial Narrow", sans-serif;
    font-weight: 700; font-size: 29px; line-height: 35px;
    color: var(--brand-green);
    text-transform: uppercase;
  }
</style>
</head>
<body>
<main class="canvas">
  <article class="flyer">
    <svg class="flyer-shapes" viewBox="0 0 586 831">
      <defs>
        <linearGradient id="beach-tones" x1="0" y1="0" x2="0" y2="1">
          <stop offset="0" stop-color="var(--sky)"/>
          <stop offset="0.5" stop-color="#8fbf9a"/>
          <stop offset="0.68" stop-color="var(--sea)"/>
          <stop offset="0.78" stop-color="var(--sand)"/>
          <stop offset="1" stop-color="#ddd2bd"/>
        </linearGradient>
      </defs>
      <path class="field-yellow" fill="var(--jam-yellow)"
        d="M0,400 C120,378 300,372 420,360 C520,345 578,270 586,190 L586,831 L0,831 Z"/>
      <path role="img" aria-label="Daytime beach with leaning coconut palms, white sand, turquoise sea and thatched huts"
        fill="url(#beach-tones)"
        d="M36,18 H553 Q569,18 569,34 V150 C550,270 470,318 360,334 C250,350 130,350 20,368 V34 Q20,18 36,18 Z"/>
      <path class="swoosh-green" fill="var(--jam-green)"
        d="M0,445 C70,395 190,372 300,364 C450,352 565,290 586,110 L586,190 C565,320 450,378 310,386 C200,394 90,430 0,560 Z"/>
      <path class="corner-black" fill="var(--flyer-black)"
        d="M262,831 C330,745 440,680 586,650 L586,831 Z"/>
      <path class="band-green" fill="var(--jam-green)"
        d="M232,831 C300,740 420,660 586,626 L586,650 C440,680 330,745 262,831 Z"/>
      <path class="brand-panel" fill="var(--white)"
        d="M572,650 V790 Q572,811 551,811 H330 Q306,811 312,790 C330,745 380,690 450,662 C500,652 545,650 572,650 Z"/>
    </svg>

    <div class="food-photo food-photo--oxtail" role="img" aria-label="Plate of stewed oxtails in rich brown gravy"></div>
    <div class="food-photo food-photo--jerk" role="img" aria-label="Jerk chicken served with rice"></div>
    <div class="food-photo food-photo--fish" role="img" aria-label="Fried fish platter with tomato, cucumber and salad"></div>

    <h1 class="headline">Your Beutiful Headline<br>Goes Here</h1>
    <p class="body-copy">Lorem Ipsum is simply dummy text of the<br>printing and typesetting industry. Lorem Ipsum<br>has been the industry's standard dummy text ever since the 1500s,<br>when an unknown printer took a galley of type and scrambled<br>it to make a type specimen book. It has survived not only five<br>centuries, but also the leap into electronic typesetting,<br>remaining essentially unchanged.</p>
    <p class="contact">Contact Us : 000-0000-000</p>
    <p class="brand-name">Mango<br>Harbor Kitchen</p>
  </article>
</main>
</body>
</html>
```